Holiday Sale 2026 Graphics for New Year

I want to create 10 social media graphics (new Instagram size 4:5 (1080 x 1350 pixels) focusing on our Holiday Sale Graphics, using any of the pics attached. Use the attached pics, NO RANDOM STOCK PHOTOGRAPHY. For the color scheme of the graphics, they should all be complementary to the product colors in the photos.
You can add any of the photos attached but none are required. You can do some of the graphics in all text. I mainly need BOLD text that says one of the headlines with the pics (10 total):
1. 25% OFF Holiday Sale: New You Starts Now!
2. 25% OFF Everything: New Year, New You
3. 25% OFF Christmas Sale 🎁 Feel Amazing Again!
4. Holiday Treat: 25% OFF Your Favorites
5. 25% OFF All Supplements ✨ New Year Reset!
6. Holiday Magic: 25% OFF Every Supplement
7. 25% OFF to Kickstart Your New Year Goals
8. New Year, New Waistline! 25% OFF Sale
9. Holiday Sale: 25% OFF Everything
10. A Better You Begins With 25% OFF

```html
<!DOCTYPE html>
<html lang="en">
<head>
<meta charset="utf-8">
<title>Holiday Sale Social Graphics</title>
<link href="https://fonts.googleapis.com/css2?family=Bebas+Neue&display=swap" rel="stylesheet">
<style>
  :root {
    --green: #1f7a4b;
    --green-deep: #136b45;
    --green-text: #2f8f55;
    --red: #a90d1c;
    --red-text: #b0132a;
    --white: #ffffff;
    --label: rgba(255,255,255,0.86);
    --page: #ffffff;
  }
  * { margin: 0; padding: 0; box-sizing: border-box; }
  html, body { width: 1200px; height: 1171px; overflow: hidden; background: var(--page); }
  body { position: relative; font-family: "Bebas Neue", "Arial Narrow", sans-serif; }

  .card {
    position: absolute;
    width: 272px;
    height: 340px;
    overflow: hidden;
    text-align: center;
    line-height: 0.95;
  }
  .card--green-top {
    background:
      radial-gradient(ellipse 75% 40% at 50% 48%, #fff 35%, rgba(255,255,255,0) 80%),
      linear-gradient(180deg, var(--green) 0%, #f4f4f4 42%, #f4f4f4 58%, var(--red) 100%);
  }
  .card--red-top {
    background:
      radial-gradient(ellipse 75% 30% at 50% 62%, #fff 35%, rgba(255,255,255,0) 80%),
      linear-gradient(180deg, var(--red) 0%, #b52c38 32%, #f0d4d7 52%, #f7f7f7 64%, var(--green) 100%);
  }
  .card--christmas {
    background:
      radial-gradient(ellipse 70% 22% at 50% 62%, #fff 40%, rgba(255,255,255,0) 85%),
      linear-gradient(180deg, var(--red) 0%, var(--red) 22%, #b83440 40%, #e7b8be 50%, #fafafa 58%, #fafafa 66%, #9cc7ac 84%, var(--green) 100%);
  }
  .card--deep-green {
    background: linear-gradient(180deg, var(--green-deep) 0%, #e8efe9 45%, #f4f4f4 62%, var(--red) 100%);
  }
  .card--deep-red {
    background: linear-gradient(180deg, var(--red) 0%, #7a1b1b 40%, #3d4a3c 62%, var(--green) 100%);
  }

  .headline { position: absolute; left: 0; right: 0; display: flex; flex-direction: column; align-items: center; }
  .line { display: block; letter-spacing: 0.5px; }
  .line--label { background: var(--label); padding: 2px 8px 0; }
  .c-green { color: var(--green-text); }
  .c-red { color: var(--red-text); }
  .c-white { color: var(--white); }

  .photo { position: absolute; }
  .photo--person-dark { background: radial-gradient(ellipse at 50% 40%, #3a302c 0%, #1c1616 55%, rgba(30,25,25,0) 75%); }
  .photo--person-light { background: radial-gradient(ellipse at 50% 45%, #efe7e2 0%, #b9a79c 45%, rgba(120,100,90,0) 75%); }
  .photo--bottles { background: radial-gradient(ellipse at 50% 55%, #ffffff 0%, #e9e9ee 45%, rgba(220,220,230,0) 78%); }
  .photo--kitchen { background: linear-gradient(90deg, #4a3328 0%, #6b4a3b 40%, rgba(150,120,110,0.6) 75%, rgba(170,30,40,0) 100%); }

  .icon { position: absolute; left: 50%; transform: translateX(-50%); }
</style>
</head>
<body>

<!-- Row 1 -->
<section class="card card--green-top" style="left:33px; top:38px;">
  <div class="headline" style="top:6px; font-size:45px;">
    <span class="line line--label c-green">Holiday Sale:</span>
    <span class="line c-red">25% Off</span>
    <span class="line line--label c-green">Everything</span>
  </div>
  <div class="photo photo--person-dark" role="img" aria-label="Woman in a black sheer top presenting three supplement bottles on a marble counter" style="left:70px; top:135px; width:135px; height:185px;"></div>
  <div class="photo" role="img" aria-label="Marble counter" style="left:0; top:316px; width:272px; height:24px; background:linear-gradient(180deg,#e8e4e2,#cfc9c6);"></div>
</section>

<section class="card card--green-top" style="left:319px; top:38px;">
  <div class="headline" style="top:56px; font-size:47px;">
    <span class="line c-green">25% Off</span>
    <span class="line c-green">To Kickstart</span>
    <span class="line c-green">Your</span>
    <span class="line line--label c-green">New Year</span>
    <span class="line line--label c-green">Goals</span>
  </div>
</section>

<section class="card card--deep-green" style="left:611px; top:38px;">
  <div class="headline" style="top:8px; font-size:47px;">
    <span class="line c-white">A Better You</span>
    <span class="line c-white">Begins With</span>
    <span class="line line--label c-green">25% Off</span>
  </div>
  <div class="photo photo--person-light" role="img" aria-label="Smiling woman in a white cropped sweater in a kitchen, presenting a row of supplement bottles" style="left:50px; top:160px; width:175px; height:180px;"></div>
</section>

<section class="card card--green-top" style="left:895px; top:38px;">
  <div class="headline" style="top:42px; font-size:47px;">
    <span class="line c-green">25% Off All</span>
    <span class="line c-green">Supplements</span>
  </div>
  <svg class="icon" style="top:144px;" width="48" height="44" viewBox="0 0 48 44" aria-hidden="true">
    <path d="M28 6 L32 18 L44 22 L32 26 L28 38 L24 26 L12 22 L24 18 Z" fill="#f4b400"/>
    <path d="M10 2 L12 7 L17 9 L12 11 L10 16 L8 11 L3 9 L8 7 Z" fill="#f4b400"/>
    <path d="M9 30 L10.5 34 L14 35 L10.5 36.5 L9 40 L7.5 36.5 L4 35 L7.5 34 Z" fill="#f4b400"/>
  </svg>
  <div class="headline" style="top:200px; font-size:51px;">
    <span class="line line--label c-red">New Year</span>
    <span class="line line--label c-red">Reset!</span>
  </div>
</section>

<!-- Row 2 -->
<section class="card card--christmas" style="left:30px; top:389px;">
  <div class="headline" style="top:40px;">
    <span class="line c-white" style="font-size:76px;">25% Off</span>
    <span class="line c-white" style="font-size:40px;">Christmas Sale</span>
  </div>
  <svg class="icon" style="top:155px;" width="40" height="42" viewBox="0 0 40 42" aria-hidden="true">
    <rect x="3" y="14" width="34" height="27" fill="#f4b400"/>
    <rect x="1" y="9" width="38" height="8" fill="#ffc928"/>
    <rect x="17" y="9" width="6" height="32" fill="#d6202c"/>
    <path d="M20 9 C12 0 6 4 10 9 Z M20 9 C28 0 34 4 30 9 Z" fill="#d6202c"/>
  </svg>
  <div class="headline" style="top:218px; font-size:47px;">
    <span class="line c-green">Feel Amazing</span>
    <span class="line c-red">Again!</span>
  </div>
</section>

<section class="card card--red-top" style="left:317px; top:389px;">
  <div class="headline" style="top:30px;">
    <span class="line c-white" style="font-size:40px;">Holiday Magic:</span>
    <span class="line c-white" style="font-size:40px;">25% Off</span>
    <span class="line line--label c-red" style="font-size:37px;">Every Supplement</span>
  </div>
  <div class="photo photo--bottles" role="img" aria-label="Four supplement bottles grouped on a white surface" style="left:20px; top:195px; width:240px; height:130px;"></div>
</section>

<section class="card card--deep-red" style="left:604px; top:389px;">
  <div class="photo photo--person-light" role="img" aria-label="Smiling woman in a white cropped sweater in a kitchen, with a row of supplement bottles in front" style="left:60px; top:60px; width:212px; height:280px;"></div>
  <div class="headline" style="top:6px; font-size:38px;">
    <span class="line c-white">New Year,</span>
    <span class="line c-white">New Waistline!</span>
  </div>
  <div class="headline" style="top:85px; left:12px; right:auto; width:88px; font-size:47px;">
    <span class="line line--label c-red">25%<br>Off<br>Sale</span>
  </div>
</section>

<section class="card" style="left:894px; top:389px; background:linear-gradient(180deg,var(--red) 0%,#8a1a1e 45%,var(--green) 100%);">
  <div class="photo photo--kitchen" role="img" aria-label="Woman in a black sheer top pointing at three supplement bottles on a marble counter" style="left:0; top:0; width:272px; height:340px;"></div>
  <div class="headline" style="top:24px; left:110px; right:0;">
    <span class="line c-white" style="font-size:42px;">25% Off</span>
    <span class="line c-white" style="font-size:30px;">Everything:</span>
  </div>
  <div class="headline" style="top:110px; left:130px; right:20px; font-size:47px;">
    <span class="line line--label c-green">New</span>
    <span class="line line--label c-green">Year,</span>
    <span class="line line--label c-green">New</span>
    <span class="line line--label c-green">You</span>
  </div>
</section>

<!-- Row 3 -->
<section class="card" style="left:317px; top:747px; background:linear-gradient(180deg,var(--red) 0%,#7e1d1e 40%,#2a3b2e 65%,var(--green) 100%);">
  <div class="headline" style="top:26px;">
    <span class="line c-white" style="font-size:44px;">Holiday Treat:</span>
    <span class="line c-white" style="font-size:66px;">25% Off</span>
    <span class="line line--label c-red" style="font-size:38px; letter-spacing:2px;">Your Favorites</span>
  </div>
  <div class="photo photo--bottles" role="img" aria-label="Supplement bottles arranged on a stone block, one lying on its side" style="left:20px; top:180px; width:240px; height:150px;"></div>
</section>

<section class="card" style="left:604px; top:747px; background:linear-gradient(180deg,var(--green-deep) 0%,#eef3ef 50%,#f4f4f4 72%,var(--red) 100%);">
  <div class="headline" style="top:16px;">
    <span class="line c-white" style="font-size:80px;">25% Off</span>
    <span class="line c-white" style="font-size:44px; letter-spacing:2px;">Holiday Sale:</span>
    <span class="line line--label c-green" style="font-size:33px; margin-top:2px;">New You Starts Now!</span>
  </div>
  <div class="photo photo--bottles" role="img" aria-label="Four supplement bottles standing in a row" style="left:15px; top:190px; width:242px; height:120px;"></div>
</section>

</body>
</html>
```